I have an existing corporate logo. I'd like to clean it up bit (sharpen it up) and make it look better (without major redesign). I'd like to get the logo itself in all major file formats for print, web, etc.
Then I'd like a business card design that reflects a strategy consulting firm. It should be clean - logo and text without major graphics, and perhaps some small color treatments that match the logo color. The card should suggest high quality in terms of the company.
I'd like the files for card in all major print formats.
Target Market(s)
Silver Birch Partners is a strategy development and business consulting firm focused on small to mid-sized companies. We specialize in business strategy, comprehensive business plan development, market segmentation and positioning, financial models, marketing and sales strategy, product strategy and the effective use of social media in business growth. We operate as consultants, advisers, retained members of management teams, and Board members. We often serve in the role of Chief Strategy Officer, supporting CEO's and other senior executives to enhance top and bottom line growth.
Our overall approach with clients is to deliver actual results, and we often take an active team role with business founders and management teams to drive business growth and affect real changes in performance. As a result, we approach each situation uniquely and partner with clients in a manner that will have the biggest impact on enterprise value.
Industry/Entity Type
Business
Look and feel

```html
<!DOCTYPE html>
<html lang="en">
<head>
<meta charset="utf-8">
<title>Silver Birch Partners – Business Card</title>
<link href="https://fonts.googleapis.com/css2?family=Arimo:wght@400;700&display=swap" rel="stylesheet">
<style>
  :root {
    --bg: #2b2b2d;
    --blue-light: #1aa3e0;
    --blue: #0a8bd0;
    --blue-deep: #0667a8;
    --brand-blue: #1d8fd6;
    --ink: #0b0b0b;
    --white: #ffffff;
    --paper: #ffffff;
    --grey: #7d7d7d;
    --muted: #6f6a66;
  }
  * { box-sizing: border-box; margin: 0; padding: 0; }
  html, body { width: 1200px; height: 800px; overflow: hidden; }
  body {
    background: var(--bg);
    font-family: "Arimo", Arial, sans-serif;
    position: relative;
  }
  .card {
    position: absolute;
    width: 480px;
    height: 272px;
    border-radius: 22px;
    overflow: hidden;
    box-shadow: 0 6px 14px rgba(0,0,0,.5);
  }
  .card--back {
    background: radial-gradient(ellipse at 85% 30%, var(--blue-light) 0%, var(--blue) 45%, var(--blue-deep) 100%);
    color: var(--white);
  }
  .card--front { background: radial-gradient(ellipse at 60% 80%, var(--blue-light) 0%, var(--blue) 50%, var(--blue-deep) 100%); color: var(--white); }
  .pos-tl { left: 100px; top: 96px; }
  .pos-tr { left: 623px; top: 96px; }
  .pos-bl { left: 100px; top: 446px; }
  .pos-br { left: 623px; top: 446px; }

  .services { position: absolute; left: 38px; top: 27px; list-style: none; font-size: 11px; line-height: 12px; }
  .services li.gap { margin-top: 12px; }
  .back-url { position: absolute; left: 38px; top: 215px; font-size: 24px; font-weight: 700; letter-spacing: .2px; }
  .back-url--dark { color: var(--ink); }
  .back-url--muted { color: var(--muted); }

  .front-art { position: absolute; inset: 0; }
  .brand {
    position: absolute; left: 40px; top: 54px;
    display: flex; align-items: center; gap: 12px;
    font-size: 24px; font-weight: 700; line-height: 24px; color: var(--brand-blue);
  }
  .brand-mark { width: 16px; height: 16px; border-radius: 50%; background: var(--brand-blue); flex: none; }
  .brand-name small { display: block; font-size: 12px; line-height: 16px; letter-spacing: 3px; }

  .person { position: absolute; left: 38px; top: 174px; }
  .person-name { font-size: 22px; font-weight: 700; line-height: 24px; color: var(--ink); }
  .person-name--muted { color: var(--muted); }
  .person-title { font-size: 12.5px; margin-top: 3px; }
  .address { position: absolute; left: 38px; top: 227px; font-size: 12.5px; line-height: 16px; }

  .contacts { position: absolute; left: 280px; top: 174px; list-style: none; font-size: 12.5px; line-height: 17px; }
  .contacts li { display: flex; align-items: center; gap: 5px; }
  .contacts .strong { font-weight: 700; }
  .icon { width: 11px; height: 11px; flex: none; }
</style>
</head>
<body>

<!-- Back, dark variant -->
<section class="card card--back pos-tl">
  <ul class="services">
    <li>- Business strategy development and planning</li>
    <li>- Identification of new market opportunities</li>
    <li>- Go-to-market strategy</li>
    <li class="gap">- Marketing and sales strategy</li>
    <li>- New business development</li>
    <li>- Comprehensive business plan development</li>
    <li class="gap">- Strategic market positioning</li>
    <li>- Operational turnarounds, improvement and stabilization</li>
    <li>- Financial justification of strategic investments</li>
    <li class="gap">- Strategic application of technology</li>
    <li>- Product portfolio analysis - profitability and prioritization</li>
    <li>- Customer insights analysis</li>
  </ul>
  <p class="back-url back-url--dark">www.sbpartners.com</p>
</section>

<!-- Front, black variant -->
<section class="card card--front pos-tr">
  <svg class="front-art" viewBox="0 0 480 272" preserveAspectRatio="none" aria-hidden="true">
    <path d="M0 0 H480 V126 Q300 168 0 140 Z" fill="#050505"/>
    <path d="M170 156 Q340 152 480 128" fill="none" stroke="#8a8a8a" stroke-width="6"/>
    <path d="M60 150 Q300 170 480 136" fill="none" stroke="#ffffff" stroke-width="1.5" opacity=".8"/>
  </svg>
  <div class="brand"><span class="brand-mark"></span><span class="brand-name">SILVER BIRCH<small>PARTNERS, LLC</small></span></div>
  <div class="person">
    <p class="person-name">Daniel M. Hartwell</p>
    <p class="person-title">Partner and Founder</p>
  </div>
  <p class="address">412 Aspen Hollow Lane<br>Westbrook, Illinois 60499</p>
  <ul class="contacts">
    <li><svg class="icon" viewBox="0 0 12 12"><rect x="2" y="0.5" width="8" height="11" rx="1.5" fill="#111"/><rect x="3.5" y="2" width="5" height="6" fill="#555"/></svg>312.555.0148</li>
    <li><svg class="icon" viewBox="0 0 12 12"><rect x="0.5" y="2" width="11" height="8" fill="#111"/><path d="M0.5 2 L6 7 L11.5 2" stroke="#888" fill="none"/></svg>daniel@sbpartners.com</li>
    <li class="strong"><svg class="icon" viewBox="0 0 12 12"><circle cx="6" cy="6" r="5.5" fill="#111"/><path d="M0.5 6 H11.5 M6 0.5 V11.5" stroke="#888"/></svg>www.sbpartners.com</li>
    <li><svg class="icon" viewBox="0 0 12 12"><rect width="12" height="12" rx="1.5" fill="#111"/></svg>linkedin.com/in/dhartwell</li>
    <li><svg class="icon" viewBox="0 0 12 12"><rect width="12" height="12" rx="1.5" fill="#111"/></svg>@DanielHartwell</li>
  </ul>
</section>

<!-- Back, muted variant -->
<section class="card card--back pos-bl">
  <ul class="services">
    <li>- Business strategy development and planning</li>
    <li>- Identification of new market opportunities</li>
    <li>- Go-to-market strategy</li>
    <li class="gap">- Marketing and sales strategy</li>
    <li>- New business development</li>
    <li>- Comprehensive business plan development</li>
    <li class="gap">- Strategic market positioning</li>
    <li>- Operational turnarounds, improvement and stabilization</li>
    <li>- Financial justification of strategic investments</li>
    <li class="gap">- Strategic application of technology</li>
    <li>- Product portfolio analysis - profitability and prioritization</li>
    <li>- Customer insights analysis</li>
  </ul>
  <p class="back-url back-url--muted">www.sbpartners.com</p>
</section>

<!-- Front, white variant -->
<section class="card card--front pos-br">
  <svg class="front-art" viewBox="0 0 480 272" preserveAspectRatio="none" aria-hidden="true">
    <path d="M0 0 H480 V126 Q300 168 0 140 Z" fill="#ffffff"/>
    <path d="M170 156 Q340 152 480 128" fill="none" stroke="#7a7a7a" stroke-width="6"/>
    <path d="M60 150 Q300 170 480 136" fill="none" stroke="#ffffff" stroke-width="1.5" opacity=".8"/>
  </svg>
  <div class="brand"><span class="brand-mark"></span><span class="brand-name">SILVER BIRCH<small>PARTNERS, LLC</small></span></div>
  <div class="person">
    <p class="person-name person-name--muted">Daniel M. Hartwell</p>
    <p class="person-title">Partner and Founder</p>
  </div>
  <p class="address">412 Aspen Hollow Lane<br>Westbrook, Illinois 60499</p>
  <ul class="contacts">
    <li><svg class="icon" viewBox="0 0 12 12"><rect x="2" y="0.5" width="8" height="11" rx="1.5" fill="#6f6a66"/><rect x="3.5" y="2" width="5" height="6" fill="#9a9590"/></svg>312.555.0148</li>
    <li><svg class="icon" viewBox="0 0 12 12"><rect x="0.5" y="2" width="11" height="8" fill="#6f6a66"/><path d="M0.5 2 L6 7 L11.5 2" stroke="#aaa" fill="none"/></svg>daniel@sbpartners.com</li>
    <li class="strong"><svg class="icon" viewBox="0 0 12 12"><circle cx="6" cy="6" r="5.5" fill="#6f6a66"/><path d="M0.5 6 H11.5 M6 0.5 V11.5" stroke="#aaa"/></svg>www.sbpartners.com</li>
    <li><svg class="icon" viewBox="0 0 12 12"><rect width="12" height="12" rx="1.5" fill="#6f6a66"/></svg>linkedin.com/in/dhartwell</li>
    <li><svg class="icon" viewBox="0 0 12 12"><rect width="12" height="12" rx="1.5" fill="#6f6a66"/></svg>@DanielHartwell</li>
  </ul>
</section>

</body>
</html>
```